Horticulture Business Card Design Project

New garden service venture, I'd like design to reflect business name, Copper Lantern garden services. Needs to be professional non comical and include a pic. I'd like to see designs in browns and greens as it will be printed on recycled paper to promote sustainability. I'd prefer a modern professonal card that is simple and catchy.
Updates

Thank u to all that submitted design/s -I really appreciated all of them.

Target Market(s)

Professional people aged between 40-60, that own their own homes and enjoy their gardens. Wanting a premium service that can be recommended to others by handing out the card and conveying a professional card that is impressive to potential clients.

Industry/Entity Type

Business

Requirements
Must have
• Picture relating to horticulture. One sided and including business name- Copper Lantern Garden Services, Qualified Horticulturist, name, mobile number and email. Website is not needed. Id like a large green leaf pic such as monstera, ficus lyrata or rhaphis palms etc. Im open to ideas and welcome new suggestions. Simple fonts please
Nice to have
• Large green leaf as pic. Possibly like monstera or similar in size and impact. A modern touch
Should not have
• Comical pic

```html
<!DOCTYPE html>
<html lang="en">
<head>
<meta charset="utf-8">
<title>Copper Lantern Garden Services — Business Card</title>
<link rel="stylesheet" href="https://fonts.googleapis.com/css2?family=Crimson+Text:wght@400;700&display=swap">
<style>
  :root {
    --bark: #3a2729;
    --paper: #ffffff;
    --leaf-light: #8fd14a;
    --leaf-mid: #4fa52a;
    --leaf-deep: #1f5a16;
  }
  html, body {
    margin: 0;
    padding: 0;
    width: 1200px;
    height: 1069px;
    overflow: hidden;
    background: var(--paper);
  }
  .canvas {
    position: relative;
    width: 1200px;
    height: 1069px;
    background: var(--paper);
  }
  .card-header {
    position: absolute;
    left: 360px;
    top: 97px;
    width: 462px;
    height: 233px;
    background: var(--bark);
    box-sizing: border-box;
    padding: 12px 0 0 11px;
    color: var(--paper);
    font-family: "Crimson Text", "Times New Roman", serif;
    font-size: 29px;
    line-height: 39px;
  }
  .card-header p { margin: 0; }
  .business-name { font-weight: 700; }
  .leaf-feature {
    position: absolute;
    left: 364px;
    top: 337px;
    width: 459px;
    height: 564px;
    box-sizing: border-box;
    border: 4px solid var(--bark);
    background:
      linear-gradient(112deg, transparent 47%, rgba(20,60,15,0.55) 52%, rgba(20,60,15,0.35) 56%, transparent 62%),
      radial-gradient(ellipse at 30% 35%, var(--leaf-light) 0%, var(--leaf-mid) 55%, var(--leaf-deep) 100%);
  }
</style>
</head>
<body>
  <main class="canvas">
    <section class="card-header">
      <p class="business-name">Copper Lantern Garden Services</p>
      <p class="contact-name">Name</p>
      <p class="contact-role">Qualified Horticulturist</p>
      <p class="contact-mobile">Mobile</p>
      <p class="contact-email">Email</p>
    </section>
    <div class="leaf-feature" role="img" aria-label="Close-up photograph of a green leaf with its central vein and fine network of veins"></div>
  </main>
</body>
</html>
```